Quality Improvement Software for healthcare agencies needs a website.

Veltrix820 is a software for hospices and home health agencies to manage their Quality Assurance Performance Improvement programs to remain complaint with the standards set by Sanovia and the Bureau of Civic Wellbeing. The web accessible software-as-a-service provides an easy, turn-key way for agencies to organize all the information they need to manage and track.

Coded - Design and coding required

4 page

```html
<!DOCTYPE html>
<html lang="en">
<head>
<meta charset="utf-8">
<title>Veltrix820 – Healthcare Software</title>
<link href="https://fonts.googleapis.com/css2?family=Poppins:wght@400;500;600;700&family=Great+Vibes&display=swap" rel="stylesheet">
<style>
:root{
  --navy:#1d3150;
  --navy-deep:#17283f;
  --ink:#1a2a40;
  --text:#3d4450;
  --muted:#5b6270;
  --sky:#2aa8f2;
  --brand:#1e8fe1;
  --pale:#eef5fd;
  --gold:#f2b705;
  --white:#ffffff;
}
*{box-sizing:border-box;margin:0;padding:0}
html,body{width:1200px;height:5195px;overflow:hidden}
body{font-family:"Poppins",sans-serif;color:var(--text);background:var(--white);position:relative}
.abs{position:absolute}
.btn{position:absolute;display:flex;align-items:center;justify-content:center;background:var(--sky);color:var(--white);font-size:12px;font-weight:500;text-decoration:none;box-shadow:0 4px 10px rgba(42,168,242,.25)}
.brand-name{font-family:"Poppins",sans-serif;font-weight:700;color:var(--ink);font-size:36px;letter-spacing:-.5px;display:flex;align-items:center;gap:10px}
.brand-name .dot{width:22px;height:22px;background:var(--brand);border-radius:3px}

/* header */
.site-header{position:absolute;top:0;left:0;width:1200px;height:100px}
.site-header .brand-name{position:absolute;left:140px;top:26px}
.main-nav{position:absolute;left:508px;top:40px;display:flex;gap:26px;font-size:13px;font-weight:500;color:var(--ink)}
.main-nav a{color:inherit;text-decoration:none}

/* hero */
.hero-welcome{left:140px;top:184px;font-family:"Great Vibes",cursive;font-size:22px;color:var(--ink)}
.hero-title{left:140px;top:226px;font-size:42px;font-weight:700;color:var(--ink)}
.hero-sub{left:140px;top:288px;font-size:35px;font-weight:500;color:var(--ink)}
.hero-text{left:140px;top:348px;width:370px;font-size:12px;line-height:20px;color:var(--text)}
.hero-art{left:525px;top:178px;width:630px;height:380px;border-radius:48% 52% 40% 44%;background:radial-gradient(circle at 50% 50%,#cfe3fb 0%,#e6f0fc 55%,rgba(255,255,255,0) 75%)}

/* about */
.about{position:absolute;top:672px;left:0;width:1200px;height:624px;background:var(--pale);overflow:hidden}
.about-wedge{position:absolute;left:0;top:0}
.about-frame{left:160px;top:92px;width:400px;height:420px;border:3px solid var(--navy);transform:skewY(-3deg)}
.about-photo{left:140px;top:112px;width:404px;height:420px;background:linear-gradient(135deg,#b9c3cc 0%,#e4e8ec 45%,#9fb6c9 100%);transform:skewY(-3deg)}
.about-title{left:630px;top:136px;font-size:27px;font-weight:500;color:var(--ink)}
.about-title span{color:var(--brand);font-weight:600;border-bottom:2px solid var(--brand)}
.about-lead{left:630px;top:194px;width:420px;font-size:14px;font-weight:600;line-height:26px;color:var(--ink)}
.about-text{left:630px;top:312px;width:420px;font-size:12px;line-height:22px;color:var(--text)}

/* features */
.section-title{position:absolute;width:1200px;text-align:center;font-size:26px;font-weight:700;color:var(--ink)}
.section-title .c1{color:var(--brand)}
.section-title .c2{color:var(--gold)}
.feature-card{position:absolute;width:292px;height:290px;background:var(--pale);border-radius:14px;text-align:center;padding:0 16px}
.feature-card svg{position:absolute;left:116px;top:70px}
.feature-card h3{position:absolute;left:0;top:152px;width:100%;font-size:15px;font-weight:500;color:var(--ink)}
.feature-card p{position:absolute;left:16px;top:180px;width:260px;font-size:11px;line-height:21px;color:var(--muted)}

/* key features */
.key{position:absolute;top:2453px;left:0;width:1200px;height:1320px;background:var(--navy)}
.key-eyebrow{left:140px;top:66px;font-size:12px;letter-spacing:6px;color:var(--white)}
.key-title{left:140px;top:92px;font-size:28px;font-weight:700;color:var(--white)}
.key-text{left:140px;top:136px;width:660px;font-size:12px;line-height:21px;color:#dfe6ef}
.key-photo{position:absolute;background:linear-gradient(135deg,#5a6f86,#a9b8c6)}
.key-item h4{position:absolute;font-size:14px;font-weight:600;color:var(--white)}
.key-item p{position:absolute;width:450px;font-size:12px;line-height:21px;color:#dfe6ef}
.read-link{position:absolute;font-size:12px;color:var(--sky);text-decoration:underline;display:flex;align-items:center;gap:6px}

/* testimonials */
.quote-card{position:absolute;top:3955px;width:408px;height:368px;background:var(--pale)}
.quote-mark{position:absolute;left:28px;top:10px;font-size:96px;line-height:1;font-weight:700;color:var(--brand)}
.stars{position:absolute;left:28px;top:92px}
.quote-card p{position:absolute;left:28px;width:360px;font-size:11.5px;line-height:16px;color:var(--text)}
.avatar{position:absolute;left:28px;top:290px;width:60px;height:60px;border-radius:50%;background:radial-gradient(circle,#d8b48e,#8c6242)}
.author{position:absolute;left:104px;top:296px;font-size:12px;line-height:20px;color:var(--ink)}
.author b{font-weight:600}
.slider-arrow{position:absolute;top:4110px;width:56px;height:56px;border-radius:50%;display:flex;align-items:center;justify-content:center}

/* cta */
.cta{position:absolute;top:4415px;left:0;width:1200px;height:355px;background:linear-gradient(180deg,#1f3553,#24405f);text-align:center;color:var(--white)}
.cta h2{position:absolute;width:100%;top:78px;font-size:28px;font-weight:700}
.cta p{position:absolute;left:210px;top:130px;width:780px;font-size:12px;line-height:21px;color:#e3eaf2}

/* footer */
.site-footer .brand-name{position:absolute;left:140px;top:4870px}
.foot-text{left:140px;top:4936px;width:340px;font-size:12px;line-height:21px;color:var(--text)}
.social{position:absolute;top:5070px;width:32px;height:32px;border:1.5px solid var(--ink);border-radius:50%}
.foot-head{position:absolute;top:4868px;font-size:22px;font-weight:500;color:var(--ink)}
.foot-links{position:absolute;left:594px;top:4918px;list-style:none;font-size:12px;color:var(--ink)}
.foot-links li{height:35.5px}
.contact-row{position:absolute;left:832px;display:flex;gap:12px;font-size:12px;line-height:20px;color:var(--ink)}
.bottom-bar{position:absolute;top:5160px;left:0;width:1200px;height:35px;background:var(--navy-deep);color:var(--white);font-size:11px}
.bottom-bar span{position:absolute;top:10px}
</style>
</head>
<body>

<header class="site-header">
  <div class="brand-name"><span class="dot"></span>Veltrix820</div>
  <nav class="main-nav">
    <a href="#">Home</a><a href="#">About Us</a><a href="#">Features</a><a href="#">Pricing</a><a href="#">Testimonials</a>
  </nav>
  <a class="btn" href="#" style="left:923px;top:28px;width:135px;height:42px">Contact Us</a>
</header>

<section class="hero">
  <div class="abs hero-welcome">Welcome To</div>
  <h1 class="abs hero-title">Veltrix820</h1>
  <div class="abs hero-sub">Healthcare Software</div>
  <p class="abs hero-text">your one-stop solution for managing and tracking your Quality Assurance Performance Improvement (QAPI) programs.</p>
  <a class="btn" href="#" style="left:140px;top:436px;width:180px;height:44px">Sign Up For A Free Trial</a>
  <div class="abs hero-art" role="img" aria-label="Illustration of clinicians working with a laptop showing charts and an insurance form"></div>
</section>

<section class="about">
  <svg class="about-wedge" width="1200" height="624" aria-hidden="true"><polygon points="0,624 1200,540 1200,624" fill="#1d3150"/></svg>
  <div class="abs about-frame"></div>
  <div class="abs about-photo" role="img" aria-label="Photo of a doctor's hands with a stethoscope and digital health icons"></div>
  <h2 class="abs about-title">About Us <span>Veltrix820</span></h2>
  <p class="abs about-lead">Our web-accessible software-as-a-service is designed to simplify the process of remaining compliant with Sanovia and Bureau of Civic Wellbeing standards.</p>
  <p class="abs about-text">At Veltrix820, we understand the importance of organizing all the necessary information in one place. That's why our software provides an easy and turn-key way for hospices and home health agencies to manage and track their QAPI programs.</p>
  <a class="btn" href="#" style="left:630px;top:433px;width:135px;height:50px">Read More</a>
</section>

<section class="features">
  <h2 class="section-title" style="top:1378px"><span class="c1">SOFT</span><span class="c2">WARE</span> FEATURES</h2>

  <div class="feature-card" style="left:140px;top:1455px">
    <svg width="60" height="60" viewBox="0 0 60 60" fill="none" stroke="#1a2a40" stroke-width="2.5"><rect x="4" y="4" width="22" height="30"/><rect x="34" y="4" width="22" height="18" stroke="#1e8fe1"/><rect x="4" y="42" width="22" height="14" stroke="#1e8fe1"/><rect x="34" y="30" width="22" height="26"/></svg>
    <h3>Dashboard</h3>
    <p>Displays an overview of the user's QAPI program, including upcoming surveys, recent reports, and staff training status</p>
  </div>
  <div class="feature-card" style="left:455px;top:1455px">
    <svg width="60" height="60" viewBox="0 0 60 60" fill="none" stroke="#1a2a40" stroke-width="2.5"><rect x="30" y="4" width="26" height="20" rx="3" fill="#7bc043"/><path d="M36 14l5 4 9-8" stroke="#fff"/><circle cx="20" cy="24" r="8"/><path d="M6 56c0-12 6-20 14-20s14 8 14 20"/><rect x="24" y="40" width="14" height="16" fill="#fff"/></svg>
    <h3>Surveys</h3>
    <p>Lists all active surveys and allows users to create new ones using predefined templates or custom forms</p>
  </div>
  <div class="feature-card" style="left:768px;top:1455px">
    <svg width="60" height="60" viewBox="0 0 60 60" fill="none" stroke="#1a2a40" stroke-width="2.5"><rect x="8" y="6" width="44" height="52" rx="3"/><rect x="20" y="2" width="20" height="8" rx="2" fill="#fff"/><path d="M16 26l6-6 6 4 10-8" stroke="#1e8fe1"/><path d="M16 36h4M24 36h20M16 44h4M24 44h20M16 52h4M24 52h20"/></svg>
    <h3>Reports</h3>
    <p>Displays a list of all closed surveys and their associated reports, with options to view or download them in various formats (PDF, Excel, CSV)</p>
  </div>
  <div class="feature-card" style="left:140px;top:1770px">
    <svg width="60" height="60" viewBox="0 0 60 60" fill="none" stroke="#1a2a40" stroke-width="2.5"><circle cx="30" cy="10" r="6" fill="#1e8fe1"/><circle cx="10" cy="18" r="5" fill="#f2b705"/><circle cx="50" cy="18" r="5" fill="#7bc043"/><path d="M4 40c0-10 3-14 6-14s6 4 6 14M44 40c0-10 3-14 6-14s6 4 6 14M20 44c0-14 4-22 10-22s10 8 10 22"/><rect x="12" y="44" width="36" height="6"/><path d="M18 50v8M42 50v8"/></svg>
    <h3>Meetings</h3>
    <p>Lists all scheduled meetings and allows users to add new ones or view past ones with notes and action items</p>
  </div>
  <div class="feature-card" style="left:455px;top:1770px">
    <svg width="60" height="60" viewBox="0 0 60 60" fill="none" stroke="#1a2a40" stroke-width="2.5"><rect x="6" y="4" width="48" height="34"/><rect x="12" y="10" width="10" height="8" fill="#1e8fe1"/><path d="M26 12h22M26 18h16M12 26h36M12 32h24"/><circle cx="20" cy="44" r="4"/><path d="M12 58c0-6 4-10 8-10s8 4 8 10"/><path d="M34 46h18v12H34z" fill="#f2b705"/></svg>
    <h3>Staff Training</h3>
    <p>Tracks individual staff members' training progress and requirements based on their roles and responsibilities</p>
  </div>
  <div class="feature-card" style="left:768px;top:1770px">
    <svg width="60" height="60" viewBox="0 0 60 60" fill="none" stroke="#1a2a40" stroke-width="2.5"><rect x="4" y="16" width="52" height="32"/><path d="M10 40l10-10 8 6 12-12 10 6" stroke="#1e8fe1"/><rect x="12" y="4" width="6" height="12" fill="#1e8fe1"/><rect x="22" y="2" width="6" height="14" fill="#f2b705"/><rect x="32" y="8" width="6" height="8" fill="#7bc043"/><path d="M22 48l-4 10M38 48l4 10M16 58h28"/></svg>
    <h3>Data Analysis</h3>
    <p>Provides tools for analyzing survey data using charts, graphs, and statistical tests to identify trends and areas for improvement</p>
  </div>
  <div class="feature-card" style="left:455px;top:2085px">
    <svg width="60" height="60" viewBox="0 0 60 60" fill="none" stroke="#1a2a40" stroke-width="3"><path d="M26 4h8l2 7 6 3 7-3 5 6-4 6 1 6 7 3v8l-7 3-1 6 4 6-6 5-6-3-6 3-2 7h-8l-2-7-6-3-6 3-6-5 4-6-1-6-7-3v-8l7-3 1-6-4-6 6-6 6 3 6-3z"/><circle cx="30" cy="30" r="9" fill="#1e8fe1" stroke="#1a2a40"/></svg>
    <h3>Settings</h3>
    <p>Allows users to customize their profile, preferences, and notifications; manage user accounts; and configure system settings like email templates and report formats</p>
  </div>
</section>

<section class="key">
  <div class="abs key-eyebrow">SOME OF THE</div>
  <h2 class="abs key-title">Key Features Of Veltrix820 Include</h2>
  <p class="abs key-text">Lorem ipsum dolor sit amet, consectetur adipiscing elit, sed do eiusmod tempor incididunt ut labore et dolore magna aliqua. Quis ipsum suspendisse ultrices gravida. Risus commodo viverra maecenas accumsan lacus vel facilisis.</p>
  <a class="btn" href="#" style="left:925px;top:137px;width:133px;height:48px">Read More</a>

  <div class="key-item">
    <div class="key-photo" style="left:140px;top:250px;width:443px;height:342px;background:linear-gradient(135deg,#e8e4dc,#c9c1b2 60%,#e9c34a)" role="img" aria-label="Photo of hands typing on a laptop showing a dashboard"></div>
    <h4 style="left:140px;top:622px">Customizable dashboards</h4>
    <p style="left:140px;top:652px">Our software allows agencies to create customized dashboards that provide a real-time view of their QAPI program's progress. This feature enables agencies to easily monitor and track performance metrics, identify areas for improvement, and take corrective action as needed.</p>
    <a class="read-link" style="left:140px;top:752px" href="#">Read More <svg width="18" height="10" viewBox="0 0 18 10" fill="none" stroke="#2aa8f2" stroke-width="1.5"><path d="M0 5h16M12 1l4 4-4 4"/></svg></a>
  </div>
  <div class="key-item">
    <div class="key-photo" style="left:612px;top:250px;width:445px;height:267px;background:linear-gradient(135deg,#3e5a76,#6f8aa3 50%,#b8946a)" role="img" aria-label="Photo of a man working at a computer with digital overlays"></div>
    <h4 style="left:612px;top:540px">Automated workflows</h4>
    <p style="left:612px;top:570px">Veltrix820 automates many of the manual processes involved in QAPI program management, such as assigning tasks, setting deadlines, and generating reports. This feature ensures that tasks are completed on time and helps agencies stay organized and efficient.</p>
    <a class="read-link" style="left:612px;top:670px" href="#">Read More <svg width="18" height="10" viewBox="0 0 18 10" fill="none" stroke="#2aa8f2" stroke-width="1.5"><path d="M0 5h16M12 1l4 4-4 4"/></svg></a>
  </div>
  <div class="key-item">
    <div class="key-photo" style="left:140px;top:805px;width:443px;height:270px;background:linear-gradient(135deg,#c9c6c0,#8e8a83 55%,#3d3a36)" role="img" aria-label="Photo of a team gathered around a table collaborating"></div>
    <h4 style="left:140px;top:1096px">Collaborative communication</h4>
    <p style="left:140px;top:1126px">Our software facilitates collaboration and communication between team members by providing a centralized platform for sharing information, documents, and feedback. This feature helps ensure that everyone is working towards the same goals and objectives.</p>
    <a class="read-link" style="left:140px;top:1226px" href="#">Read More <svg width="18" height="10" viewBox="0 0 18 10" fill="none" stroke="#2aa8f2" stroke-width="1.5"><path d="M0 5h16M12 1l4 4-4 4"/></svg></a>
  </div>
  <div class="key-item">
    <div class="key-photo" style="left:612px;top:715px;width:445px;height:344px;background:linear-gradient(135deg,#f1f3f5,#cfd6dd 55%,#8aa0b6)" role="img" aria-label="Photo of a tablet showing bar charts on top of printed reports"></div>
    <h4 style="left:612px;top:1086px">Customizable dashboards</h4>
    <p style="left:612px;top:1116px">Veltrix820 generates detailed reports that provide insights into performance trends, identify areas for improvement, and help agencies demonstrate compliance with Sanovia and Bureau of Civic Wellbeing standards. This feature allows agencies to make data-driven decisions and continuously improve their QAPI programs.</p>
    <a class="read-link" style="left:612px;top:1236px" href="#">Read More <svg width="18" height="10" viewBox="0 0 18 10" fill="none" stroke="#2aa8f2" stroke-width="1.5"><path d="M0 5h16M12 1l4 4-4 4"/></svg></a>
  </div>
</section>

<section class="testimonials">
  <h2 class="section-title" style="top:3866px">CLIENT <span class="c1">TESTI</span><span class="c2">MONIALS</span></h2>

  <a class="slider-arrow" href="#" style="left:77px;border:2px solid var(--ink)" aria-label="Previous"><svg width="14" height="22" viewBox="0 0 14 22" fill="none" stroke="#1a2a40" stroke-width="2"><path d="M12 2L3 11l9 9"/></svg></a>
  <a class="slider-arrow" href="#" style="left:1067px;background:var(--navy)" aria-label="Next"><svg width="14" height="22" viewBox="0 0 14 22" fill="none" stroke="#fff" stroke-width="2"><path d="M2 2l9 9-9 9"/></svg></a>

  <div class="quote-card" style="left:178px">
    <div class="quote-mark">“</div>
    <svg class="stars" width="120" height="20" viewBox="0 0 120 20" fill="#1a2a40"><g id="star"><path d="M10 1l2.6 5.6 6 .6-4.5 4 1.3 6L10 14.2 4.6 17.2l1.3-6-4.5-4 6-.6z"/></g><use href="#star" x="24"/><use href="#star" x="48"/><use href="#star" x="72"/><use href="#star" x="96"/></svg>
    <p style="top:130px">Lorem ipsum dolor sit amet, consectetur adipiscing elit, sed do eiusmod tempor incididunt ut labore et dolore magna aliqua. Quis ipsum suspendisse ultrices gravida. Risus commodo viverra maecenas accumsan lacus vel facilisis.</p>
    <p style="top:220px">Lorem ipsum dolor sit amet, consectetur adipiscing elit, sed do eiusmod tempor incididunt ut labore et dolore.</p>
    <div class="avatar" role="img" aria-label="Client portrait"></div>
    <div class="author"><b>– MAREN OAKLEY</b><br>Larkfield, Westmoor</div>
  </div>
  <div class="quote-card" style="left:615px">
    <div class="quote-mark">“</div>
    <svg class="stars" width="120" height="20" viewBox="0 0 120 20" fill="#1a2a40"><use href="#star"/><use href="#star" x="24"/><use href="#star" x="48"/><use href="#star" x="72"/><use href="#star" x="96"/></svg>
    <p style="top:130px">Lorem ipsum dolor sit amet, consectetur adipiscing elit, sed do eiusmod tempor incididunt ut labore et dolore magna aliqua. Quis ipsum suspendisse ultrices gravida. Risus commodo viverra maecenas accumsan lacus vel facilisis.</p>
    <p style="top:220px">Lorem ipsum dolor sit amet, consectetur adipiscing elit, sed do eiusmod tempor incididunt ut labore et dolore.</p>
    <div class="avatar" role="img" aria-label="Client portrait"></div>
    <div class="author"><b>– MAREN OAKLEY</b><br>Larkfield, Westmoor</div>
  </div>
</section>

<section class="cta">
  <h2>AT VELTRIX820</h2>
  <p>we are committed to providing our clients with the best possible software solution for managing their QAPI programs. Our software is designed to be intuitive, user-friendly, and customizable to meet the unique needs of each agency. If you have any questions or would like to learn more about our software, please don't hesitate to</p>
  <a class="btn" href="#" style="left:505px;top:235px;width:188px;height:43px">Sign Up For A Free Trial</a>
</section>

<footer class="site-footer">
  <div class="brand-name"><span class="dot"></span>Veltrix820</div>
  <p class="abs foot-text">Lorem ipsum dolor sit amet, consectetur adipiscing elit, sed do eiusmod tempor incididunt ut labore et dolore magna aliqua. Quis ipsum suspendisse ultrices gravida. Risus commodo viverra maecenas accumsan lacus vel facilisis.</p>
  <a class="social" href="#" style="left:144px" aria-label="Social profile 1"></a>
  <a class="social" href="#" style="left:191px" aria-label="Social profile 2"></a>
  <a class="social" href="#" style="left:238px" aria-label="Social profile 3"></a>
  <a class="social" href="#" style="left:284px" aria-label="Social profile 4"></a>

  <h3 class="foot-head" style="left:585px">Quick Links</h3>
  <ul class="foot-links">
    <li>Home</li><li>About Us</li><li>Features</li><li>Pricing</li><li>Testimonials</li><li>Contact Us</li>
  </ul>

  <h3 class="foot-head" style="left:832px">Contact Info</h3>
  <div class="contact-row" style="top:4918px"><svg width="16" height="20" viewBox="0 0 16 20" fill="none" stroke="#1a2a40" stroke-width="1.5"><path d="M8 19s-7-7-7-11a7 7 0 0114 0c0 4-7 11-7 11z"/><circle cx="8" cy="8" r="2.5"/></svg><span>Address 1, Address 2, Address 3,<br>Address 4.</span></div>
  <div class="contact-row" style="top:4988px"><svg width="16" height="16" viewBox="0 0 16 16" fill="none" stroke="#1a2a40" stroke-width="1.5"><path d="M3 1l3 3-2 2c1 2 4 5 6 6l2-2 3 3-2 2C7 15 1 9 1 3z"/></svg><span>0100 555 0199</span></div>
  <div class="contact-row" style="top:5030px"><svg width="16" height="14" viewBox="0 0 16 14" fill="none" stroke="#1a2a40" stroke-width="1.5"><rect x="1" y="1" width="14" height="12"/><path d="M1 1l7 6 7-6"/></svg><span>hello@veltrix820care</span></div>

  <div class="bottom-bar">
    <span style="left:140px">©2023 Veltrix820 Healthcare Software</span>
    <span style="left:793px">PRIVACY TERMS &nbsp;&nbsp; | &nbsp;&nbsp; TERMS &amp; CONDITIONS</span>
  </div>
</footer>

</body>
</html>
```